New letter head for Air Conditioning business

We need a new professional letter head design to suit our new re-branded air conditioning business. Our new logo is attached

```html
<!DOCTYPE html>
<html lang="en">
<head>
<meta charset="utf-8">
<title>Northvale Air Conditioning &amp; Refrigeration — Letterhead</title>
<link rel="stylesheet" href="https://fonts.googleapis.com/css2?family=Open+Sans:wght@400;600;700&family=Allura&display=swap">
<style>
  :root {
    --canvas: #ecebea;
    --paper: #ffffff;
    --ink: #3a3a3a;
    --ink-soft: #555555;
    --brand-dark: #2f3133;
    --brand-green: #4cb877;
    --brand-red: #e9573f;
  }
  * { box-sizing: border-box; margin: 0; padding: 0; }
  html, body {
    width: 1200px;
    height: 900px;
    overflow: hidden;
    background: var(--canvas);
    font-family: "Open Sans", Arial, sans-serif;
    color: var(--ink);
  }
  .letterhead {
    position: absolute;
    left: 296px;
    top: 20px;
    width: 608px;
    height: 860px;
    background: var(--paper);
    box-shadow: 0 6px 24px rgba(0,0,0,0.12);
    padding: 54px 66px 0 66px;
  }
  .brand {
    display: flex;
    align-items: center;
    gap: 12px;
  }
  .brand-dot {
    width: 30px;
    height: 30px;
    border-radius: 50%;
    background: var(--brand-green);
    flex: none;
  }
  .brand-name {
    font-size: 30px;
    font-weight: 700;
    letter-spacing: 3px;
    color: var(--brand-dark);
    line-height: 1;
  }
  .brand-tagline {
    margin: 6px 0 0 42px;
    font-size: 7.5px;
    font-weight: 600;
    letter-spacing: 1.6px;
    color: var(--brand-green);
    text-transform: uppercase;
  }
  .letter-date {
    margin-top: 58px;
    font-size: 11px;
  }
  .recipient {
    margin-top: 18px;
    margin-left: 10px;
    font-size: 11px;
    line-height: 1.35;
  }
  .salutation {
    margin-top: 42px;
    margin-left: 52px;
    font-size: 11px;
    font-weight: 700;
  }
  .letter-body {
    margin-top: 22px;
    margin-left: 52px;
    font-size: 10.5px;
    line-height: 1.55;
    color: var(--ink-soft);
  }
  .letter-body p + p { margin-top: 18px; }
  .sign-off {
    margin-top: 54px;
    margin-left: 52px;
    font-size: 10.5px;
    color: var(--ink-soft);
  }
  .signature {
    font-family: "Allura", cursive;
    font-size: 32px;
    color: var(--ink);
    margin-top: 2px;
    line-height: 1.1;
  }
  .signer-name {
    font-size: 11px;
    font-weight: 700;
    color: var(--ink);
    margin-top: 2px;
  }
  .signer-company {
    font-size: 10.5px;
    color: var(--ink-soft);
  }
  .contact-footer {
    position: absolute;
    left: 118px;
    bottom: 44px;
    font-size: 10px;
    line-height: 1.45;
    color: var(--ink);
  }
  .contact-company {
    color: var(--brand-green);
    text-transform: uppercase;
    font-size: 10.5px;
  }
  .contact-label { color: var(--brand-red); }
</style>
</head>
<body>
  <main class="letterhead">
    <header>
      <div class="brand">
        <span class="brand-dot"></span>
        <span class="brand-name">NORTHVALE</span>
      </div>
      <div class="brand-tagline">Air Conditioning &amp; Refrigeration</div>
    </header>

    <p class="letter-date">10 September, 2020</p>

    <address class="recipient" style="font-style: normal;">
      Mr, Daniel R. Whitford<br>
      President<br>
      Brightline Holdings<br>
      2750 Maple Ridge Rd, Ashford,<br>
      VA 22190-4410
    </address>

    <p class="salutation">Dear Mr Daniel</p>

    <section class="letter-body">
      <p>Contrary to popular belief, Lorem Ipsum is not simply random text. It has roots in a piece of classical Latin literature from 45 BC, making it over 2000 years old. Richard McClintock, a Latin professor at Hampden-Sydney College in Virginia, looked up one of the more obscure Latin words, consectetur, from a Lorem Ipsum passage, and going through the cites of the word in classical literature, discovered the undoubtable source.</p>
      <p>Lorem Ipsum comes from sections 1.10.32 and 1.10.33 of "de Finibus Bonorum et Malorum" (The Extremes of Good and Evil) by Cicero, written in 45 BC. This book is a treatise on the theory of ethics, very popular during the Renaissance. Lorem Ipsum used since the 1500s is reproduced below for those interested. Sections 1.10.32 and 1.10.33 from "de Finibus Bonorum et Malorum" by Cicero are also reproduced in</p>
      <p>Contrary to popular belief, Lorem Ipsum is not simply random text. It has roots in a piece of classical Latin literature from 45 BC, making it over 2000 years old. Richard McClintock, a Latin professor at Hampden-Sydney College in Virginia, looked up one of the more obscure Latin words.</p>
    </section>

    <section class="sign-off">
      <p>Sincerely your</p>
      <p class="signature">Your Name</p>
      <p class="signer-name">Martin L. Carver</p>
      <p class="signer-company">Company name</p>
    </section>

    <footer class="contact-footer">
      <p class="contact-company">Northvale Air Conditioning &amp; Refrigeration</p>
      <p>418 Orchard Ln, Millbrook,</p>
      <p><span class="contact-label">Tel:</span>(555)010-2040 <span class="contact-label">Fax:</span>(555)010-2041</p>
      <p><span class="contact-label">Email:</span>hello@northvaleair.example</p>
    </footer>
  </main>
</body>
</html>
```